Business Cards for Tech Company - uBrightowl

We would like new modern business cards designed for our company. Attached are some examples of other business cards we like. <br/><br/>Info we need is: <br/>First Name, Last Name<br/>Address<br/>Store Phone<br/>Cell Phone<br/>Email Address<br/>Text Logo <br/>And Other Logo<br/>

Industry/Entity Type

Technology Equipment

Contact Information for Business Card

Please use these details as example:

Dale Morrow
Technology Specialist
Direct 555.617.2094
Phone 555-730-8186

dale.morrow@ubrightowl.example

2971 Willet Lane
Harlow Springs, NE 00427

Font styles to use
Sans Serif
Other font styles liked:
• Anything easy to read and modern

Colors

Designer to choose colors to be used in the design.

Requirements
Must have
• Both Logos
• Signature as name
• Use the text logo and use the shark logo but do not use the full shark logo. Have it where it is zoomed in and is expanding out of the card.
Nice to have
• Keep it clean and modern
• We like blue, white, and black/grays.
Should not have
• Random icons for phone and address.

```html
<!DOCTYPE html>
<html lang="en">
<head>
<meta charset="utf-8">
<title>uBrightowl Business Card</title>
<link rel="stylesheet" href="https://fonts.googleapis.com/css2?family=Play:wght@400;700&family=Arimo:wght@400&display=swap">
<style>
  :root {
    --sheet: #ffffff;
    --frame: #000000;
    --card-light: #e7e7e7;
    --card-edge: #222222;
    --brand-blue: #3463ae;
    --charcoal: #3b3b3d;
    --ink: #000000;
    --white: #ffffff;
  }
  * { margin: 0; padding: 0; box-sizing: border-box; }
  html, body { width: 957px; height: 1200px; overflow: hidden; background: var(--sheet); }
  .sheet {
    position: relative; width: 957px; height: 1200px;
    border: 8px solid var(--frame); background: var(--sheet);
  }
  .card { position: absolute; overflow: hidden; }
  .card--front {
    left: 78px; top: 71px; width: 783px; height: 497px;
    background: var(--card-light); border: 1px solid var(--card-edge);
  }
  .band { position: absolute; left: 98px; width: 589px; height: 16px; }
  .band--top { top: 0; background: var(--brand-blue); }
  .band--bottom { bottom: 0; background: var(--charcoal); }
  .wordmark {
    position: absolute; font-family: "Play", sans-serif; font-weight: 700;
    letter-spacing: -1px; line-height: 1; white-space: nowrap;
  }
  .card--front .wordmark { left: 204px; top: 84px; font-size: 66px; color: var(--brand-blue); }
  .identity { position: absolute; left: 74px; top: 280px; font-family: "Play", sans-serif; }
  .identity__name { font-size: 32px; font-weight: 700; color: var(--brand-blue); line-height: 1; letter-spacing: 0.5px; }
  .identity__role { font-size: 21px; color: var(--charcoal); margin-top: 8px; letter-spacing: 0.6px; }
  .divider { position: absolute; left: 440px; top: 271px; width: 2px; height: 86px; background: var(--ink); }
  .contact {
    position: absolute; left: 473px; top: 268px;
    font-family: "Arimo", sans-serif; font-size: 19px; color: var(--ink); line-height: 24px;
    white-space: nowrap;
  }
  .contact__email { margin-top: 15px; font-size: 18px; }
  .address {
    position: absolute; left: 0; right: 0; top: 426px; text-align: center;
    font-family: "Arimo", sans-serif; font-size: 19px; color: var(--ink); white-space: nowrap;
  }
  .card--back { left: 80px; top: 619px; width: 782px; height: 496px; background: var(--ink); }
  .card--back .wordmark { left: 82px; top: 214px; font-size: 58px; color: var(--white); }
  .emblem-area { position: absolute; right: 0; top: 0; width: 298px; height: 496px; }
</style>
</head>
<body>
<main class="sheet">
  <section class="card card--front" aria-label="Card front">
    <div class="band band--top"></div>
    <div class="wordmark">uBrightowl</div>
    <div class="identity">
      <p class="identity__name">Dale Morrow</p>
      <p class="identity__role">Technology Specialist</p>
    </div>
    <div class="divider"></div>
    <div class="contact">
      <p>555.617.2094 (Direct)</p>
      <p>555-730-8186</p>
      <p class="contact__email">dale.morrow@ubrightowl.example</p>
    </div>
    <p class="address">2971 Willet Lane, Harlow Springs, NE 00427</p>
    <div class="band band--bottom"></div>
  </section>

  <section class="card card--back" aria-label="Card back">
    <div class="wordmark">uBrightowl</div>
    <svg class="emblem-area" viewBox="0 0 298 496" role="img" aria-label="Large zoomed-in brand emblem bleeding off the card edge">
      <defs>
        <linearGradient id="emblemTone" x1="0" y1="0" x2="1" y2="0">
          <stop offset="0" stop-color="#5b6585"/>
          <stop offset="1" stop-color="#606060"/>
        </linearGradient>
      </defs>
      <rect width="298" height="496" fill="url(#emblemTone)"/>
    </svg>
  </section>
</main>
</body>
</html>
```